Wine labels Velmora Wine Council - Nueva etiqueta El Consejo Regulador de vinos de Albarrán

Velmora Wines Council, based in southern Spain, are looking to create a new suite of wine labels which retain the elegance of the Sherry Wines industry while reinvigorating their image to the modern era and a new generation of Sherry Wine lovers. These labels will be used across the Velmora Wines Council's range of wines for the promotion of the Sherry Wines industry.

Your design must present at least two styles of Sherry Wines which demonstrate an elegant, modern interpretation and understanding of the unique mood and personality for these wines and the essence of southern Spain.

10 labels will be created based on the winning design, one for each of the unique varieties of Sherry Wines within the collection. This collection comprises of several different wine varieties including: Fino, Manzanilla, Amontillado, Oloroso, Palo Cortado, Medium, Cream, Pale Cream, Pedro Ximenez and Moscatel.

We recommend you visit our website www.velmora-vinos.example/wines as the source to understanding the origins and unique personality of these diverse wines.

El Consejo Regulador de los Vinos de Albarrán y Tordesal quiere renovar las etiquetas de los vinos utilizados para sus actividades de promoción genérica. Esta colección de vinos comprende las tipologías más importantes de la región que incluye: fino, manzanilla, amontillado, oloroso, palo cortado, pale cream, medium, cream, pedro ximénez y moscatel. Por lo tanto se precisan 10 etiquetas, una para cada uno de los vinos mencionados.
Updates

Project Deadline Extended
Reason: Due to some confusion with the deadline we wish to officially extend the deadline to allow designers one last week to submit their entries.

Target Market(s)

Industry, journalists, media, sommeliers, chefs, wine writers

Industry/Entity Type

Council

Requirements
Must have
• Front and Back label plus capsule:
• Front label can have either of the two official logos of the Velmora Wine council titled Vinos de Albarrán Digital or not, this is optional. Must include: Vino selecionado por el Consejo Regulador de la Denominacion de Origen, Name of the variety of wine eg FINO, percentage of alcohol eg 15% and quantity 75 cl.
• The back of the label must include the council logo titled Sellora and 4 additional logos positioned smaller. The Europa logo must appear larger than the 3 other logos. Space for descriptive text about the wine is also required.
• The dimensions of the bottle can be found at this link http://www.vidrialto.example/es/catalogo/vinos-y-espumosos/bordelesas/bd-orla
• Altura:305 mm
• Diámetro base:76,20 mm
• Diámetro hombro:82 mm
• Tipo boca:Cetie
• Peso:750 gr
• Capacidad:75 cl
• Etiqueta delantera y trasera y capsula
• La etiqueta delantera puede incluir el logo oficial del Consejo Regulador o el logo digital, o ninguno, esto es opcional. Debe incluir el siguiete texto: Vino selecionado por el Consejo Regulador de la Denominacion de Origen, el nombre de la variedad del vino, por ejemplo Fino, el porcentaje de alcohol, por ejemplo 15%, y la capacidad 75cl.
• La etiqueta trasera debe incluir el logo oficial Sellora del Consejo, y cuatro logos adicionales con una dimension menor. El Logo de ¨Europa invierte en las zonas rurales¨ debe ser de mayor tamaño que los otros. Se precisa espacio para el texto descriptivo de los vinos.
• Las dimensiones de la botella se puede encontrar en este enlace
• http://www.vidrialto.example/es/catalogo/vinos-y-espumosos/bordelesas/bd-orla
• Altura:305 mm
• Diámetro base:76,20 mm
• Diámetro hombro:82 mm
• Tipo boca:Cetie
• Peso:750 gr
• Capacidad:75 cl
Nice to have
• See our website velmora-vinos.example to understand the origin of the wines. Ver nuestra página web velmora-vinos.example para mejor entender los vinos.
Should not have
• Images of catavinos or stereotypical images from Spain such as flamenco dancers or guitars.

```html
<!DOCTYPE html>
<html lang="en">
<head>
<meta charset="utf-8">
<title>Velmora Manzanilla – Back Label</title>
<link href="https://fonts.googleapis.com/css2?family=Mulish:wght@400;800&display=swap" rel="stylesheet">
<style>
  :root {
    --paper: #ffffff;
    --ink: #1d1d1b;
    --badge-green: #1f7a3a;
    --badge-soft: #e6efe8;
    --badge-line: #1d1d1b;
  }
  html, body {
    margin: 0;
    padding: 0;
    width: 1200px;
    height: 2400px;
    overflow: hidden;
    background: var(--paper);
  }
  .back-label {
    position: relative;
    width: 1200px;
    height: 2400px;
    background: var(--paper);
    color: var(--ink);
    font-family: "Mulish", "Helvetica Neue", Arial, sans-serif;
    font-size: 34px;
    line-height: 52px;
  }
  .council-mark {
    position: absolute;
    left: 820px;
    top: 150px;
    width: 290px;
    height: 400px;
    display: flex;
    flex-direction: column;
    align-items: center;
    justify-content: center;
    gap: 28px;
  }
  .council-mark__square {
    width: 40px;
    height: 40px;
    background: var(--ink);
  }
  .council-mark__name {
    font-size: 58px;
    font-weight: 400;
    letter-spacing: 6px;
    line-height: 1;
  }
  .wine-intro {
    position: absolute;
    left: 86px;
    top: 244px;
    margin: 0;
  }
  .wine-text {
    position: absolute;
    left: 86px;
    top: 660px;
    width: 1040px;
  }
  .wine-text p {
    margin: 0 0 50px;
  }
  .wine-text strong {
    font-weight: 800;
  }
  .partner-main {
    position: absolute;
    left: 249px;
    top: 1671px;
  }
  .partner-row {
    position: absolute;
    left: 240px;
    top: 2118px;
  }
</style>
</head>
<body>
  <main class="back-label">
    <div class="council-mark">
      <div class="council-mark__square"></div>
      <div class="council-mark__name">VELMORA</div>
    </div>

    <p class="wine-intro">
      Manzanilla is a dry white wine made<br>
      from palomino grapes and aged<br>
      under a layer of yeasts know as veil<br>
      de flor. It is produced exclusively in<br>
      the bodegas of Sanlúcar de<br>
      Barrameda. The special climatic<br>
      conditions of the town, situated at the<br>
      mouth of the river Guadalquivar,
    </p>

    <div class="wine-text">
      <p>favour the formation of a special kind of veil of flor which gives the wine its uniquely distinctive characteristics.</p>
      <p><strong>ALWAYS SERVE VERY CHILLED:</strong> Use an ice bucket with both ice and water to serve chilled between 6 &amp; 8º C.</p>
      <p><strong>THE WINE OF THE SEA:</strong> Perfect with fish, seafood and all styles of food from the sea.</p>
      <p><strong>STYLE OF GLASS:</strong> In traditional wide rimmed catavinos or in a white wine glass.</p>
    </div>

    <svg class="partner-main" width="686" height="310" viewBox="0 0 686 310" role="img" aria-label="Rural development funding badge">
      <rect x="0" y="0" width="686" height="310" rx="24" fill="var(--badge-soft)"/>
    </svg>

    <svg class="partner-row" width="700" height="192" viewBox="0 0 700 192" role="img" aria-label="Partner and certification badges">
      <rect x="0" y="2" width="166" height="186" fill="var(--badge-soft)"/>
      <rect x="223" y="16" width="257" height="140" fill="var(--badge-soft)"/>
      <circle cx="617" cy="77" r="76" fill="none" stroke="var(--badge-line)" stroke-width="3"/>
    </svg>
  </main>
</body>
</html>
```